Law firm business card

Information:

Me Marisa Delacourt

website: velmont-juris.ca
email: marisa@velmont-juris.ca
Phone: 514 372-5106
Fax: 514 372-5107

Address:
Delacourt and associates
2917 Brisebois
Montreal, QC
H3K 2T9

Areas of Expertise:
Franchise Agreements, Financing, Acquisition, Real Estate Development, Commercial Agreements and Corporate Law

Target Market(s)

executives, companie managers

Industry/Entity Type

Business

Colors
f78f20
000000

Requirements
Must have
• Must use the logo, the logo is available here:

https://www.filevault-share.net/sh/qe82kd0pl1m7/BXtr9LmQw3zPaYkN

```html
<!DOCTYPE html>
<html lang="en">
<head>
<meta charset="utf-8">
<title>Delacourt and associates – business card</title>
<link rel="stylesheet" href="https://fonts.googleapis.com/css2?family=Exo+2:wght@400;500;600&display=swap">
<style>
  :root {
    --orange: #f78f20;
    --ink: #1a1a1a;
    --grey-band: #6b6b6b;
    --grey-tab: #555555;
    --paper: #ffffff;
    --backdrop: #eceded;
    --muted: #e6e6e6;
  }
  * { box-sizing: border-box; margin: 0; padding: 0; }
  html, body { width: 1200px; height: 975px; overflow: hidden; }
  body {
    background: var(--backdrop);
    font-family: "Exo 2", "Segoe UI", sans-serif;
    color: var(--ink);
    position: relative;
  }
  .card {
    position: absolute;
    top: 137px;
    width: 400px;
    height: 700px;
    background: var(--paper);
    border-radius: 26px;
    overflow: hidden;
    box-shadow: 0 14px 30px rgba(0,0,0,.18), 0 2px 6px rgba(0,0,0,.12);
  }
  .card--front { left: 160px; }
  .card--back { left: 640px; }

  /* firm name block */
  .firm-name {
    display: flex;
    align-items: center;
    gap: 14px;
    color: var(--orange);
    font-weight: 500;
    letter-spacing: .06em;
    text-transform: uppercase;
    line-height: 1.1;
  }
  .firm-name__dot {
    flex: none;
    border: 2px solid var(--orange);
    border-radius: 50%;
  }

  .card--front .firm-name {
    position: absolute;
    top: 78px;
    left: 40px;
    font-size: 22px;
  }
  .card--front .firm-name__dot { width: 46px; height: 46px; }

  .contact-block {
    position: absolute;
    left: 0;
    width: 100%;
    padding: 0 46px;
    font-size: 21px;
    font-weight: 500;
    letter-spacing: .03em;
    line-height: 1.45;
  }
  .contact-block--phones { top: 242px; }
  .contact-block--online { top: 362px; font-size: 19px; }
  .contact-block--address { top: 482px; font-size: 19px; }

  .rule {
    position: absolute;
    left: 0;
    width: 100%;
    height: 3px;
    background: var(--orange);
  }
  .rule--1 { top: 220px; }
  .rule--2 { top: 340px; }
  .rule--3 { top: 460px; }

  .name-band {
    position: absolute;
    left: 0;
    bottom: 0;
    width: 100%;
    height: 132px;
    background: var(--orange);
    color: var(--paper);
    padding: 30px 40px 0;
  }
  .name-band__name {
    font-size: 30px;
    font-weight: 600;
    letter-spacing: .06em;
    text-transform: uppercase;
  }
  .name-band__title {
    font-size: 17px;
    letter-spacing: .12em;
    text-transform: uppercase;
    margin-top: 4px;
  }

  /* back */
  .card--back .firm-name {
    position: absolute;
    top: 190px;
    left: 0;
    width: 100%;
    justify-content: center;
    font-size: 26px;
  }
  .card--back .firm-name__dot { width: 54px; height: 54px; }

  .web-band {
    position: absolute;
    left: 0;
    bottom: 0;
    width: 100%;
    height: 210px;
  }
  .web-band svg { position: absolute; inset: 0; }
  .web-band__url {
    position: absolute;
    left: 0;
    bottom: 58px;
    width: 100%;
    text-align: center;
    color: #2b2b2b;
    font-size: 20px;
    letter-spacing: .06em;
  }
</style>
</head>
<body>

  <section class="card card--front" aria-label="Business card front">
    <div class="firm-name">
      <span class="firm-name__dot"></span>
      <span>Delacourt<br>and associates</span>
    </div>

    <span class="rule rule--1"></span>
    <div class="contact-block contact-block--phones">
      <p>T&nbsp; 514 372-5106</p>
      <p>F&nbsp; 514 372-5107</p>
    </div>

    <span class="rule rule--2"></span>
    <div class="contact-block contact-block--online">
      <p>marisa@velmont-juris.ca</p>
      <p>velmont-juris.ca</p>
    </div>

    <span class="rule rule--3"></span>
    <div class="contact-block contact-block--address">
      <p>2917 Brisebois,</p>
      <p>Montreal, QC H3K 2T9</p>
    </div>

    <div class="name-band">
      <p class="name-band__name">Marisa Delacourt</p>
      <p class="name-band__title">General Manager</p>
    </div>
  </section>

  <section class="card card--back" aria-label="Business card back">
    <div class="firm-name">
      <span class="firm-name__dot"></span>
      <span>Delacourt<br>and associates</span>
    </div>

    <div class="web-band">
      <svg width="400" height="210" viewBox="0 0 400 210" aria-hidden="true">
        <path d="M0 40 H160 L180 0 H220 L240 40 H400 V210 H0 Z" fill="var(--grey-band)"/>
        <polygon points="200,18 219,29 219,51 200,62 181,51 181,29" fill="var(--grey-tab)" stroke="#3e3e3e" stroke-width="2"/>
        <g fill="none" stroke="#2a2a2a" stroke-width="1.6">
          <circle cx="200" cy="40" r="11"/>
          <ellipse cx="200" cy="40" rx="5" ry="11"/>
          <line x1="189" y1="40" x2="211" y2="40"/>
          <line x1="191" y1="34" x2="209" y2="34"/>
          <line x1="191" y1="46" x2="209" y2="46"/>
        </g>
      </svg>
      <p class="web-band__url">velmont-juris.ca</p>
    </div>
  </section>

</body>
</html>
```